July 4th Postcard to existing clients

5x7 postcard wishing our clients happy 4th of July. Card should read on the back "Thank You For Being A Valued Client!. Stay Safe And Enjoy Your Independence Day Celebrations!"

Patriotic theme with fireworks is ideal. We are a law firm so should still have a feel of professionalism while still being fun since it is for a fun holiday.

```html
<!DOCTYPE html>
<html lang="en">
<head>
<meta charset="utf-8">
<title>Happy 4th of July Postcard – Brightwater Counsel</title>
<link href="https://fonts.googleapis.com/css2?family=Lobster&family=Tenor+Sans&display=swap" rel="stylesheet">
<style>
  :root {
    --page-bg: #e6e6e6;
    --card-dark: #0d0509;
    --patriot-red: #a60d12;
    --patriot-blue: #4c12d6;
    --star-white: #ffffff;
    --text-white: #ffffff;
    --text-dark: #2e2e34;
    --stamp-grey: #dcdcdc;
    --line-grey: #6e6e6e;
  }
  * { box-sizing: border-box; margin: 0; padding: 0; }
  html, body { width: 960px; height: 1200px; overflow: hidden; }
  body { background: var(--page-bg); position: relative; font-family: "Tenor Sans", sans-serif; }

  .postcard { position: absolute; left: 97px; width: 767px; height: 548px; overflow: hidden; }
  .postcard--front { top: 36px; background: var(--card-dark); }
  .postcard--back { top: 607px; background: #ffffff; }

  .front-artwork {
    position: absolute; inset: 0;
    background:
      radial-gradient(ellipse 200px 160px at 300px 110px, rgba(120,60,130,0.75), transparent 70%),
      radial-gradient(ellipse 150px 200px at 90px 200px, rgba(140,40,50,0.55), transparent 70%),
      radial-gradient(ellipse 140px 200px at 680px 170px, rgba(150,40,50,0.55), transparent 70%),
      radial-gradient(ellipse 260px 160px at 420px 80px, rgba(70,30,110,0.5), transparent 75%),
      var(--card-dark);
  }

  .firm-name { position: absolute; display: flex; align-items: center; justify-content: center; gap: 10px;
               white-space: nowrap; font-family: "Tenor Sans", sans-serif; font-weight: 400; }
  .firm-name__dot { width: 10px; height: 10px; border-radius: 50%; background: currentColor; }
  .firm-name--front { left: 0; right: 0; top: 268px; font-size: 24px; color: var(--text-white); }
  .firm-name--back { left: 418px; width: 222px; top: 82px; font-size: 19px; color: var(--text-dark); }

  .star-row { position: absolute; left: 238px; width: 307px; height: 16px;
              display: flex; justify-content: space-between; }
  .star-row svg { width: 16px; height: 16px; }
  .star-row--top { top: 414px; top: 322px; }
  .star-row--bottom { top: 518px; }

  .rule { position: absolute; height: 6px; }
  .rule--red { background: var(--patriot-red); left: 223px; width: 336px; }
  .rule--white { background: var(--star-white); left: 189px; width: 402px; }
  .rule--blue { background: var(--patriot-blue); left: 125px; width: 532px; }
  .rule--top.rule--red { top: 345px; }
  .rule--top.rule--white { top: 355px; }
  .rule--top.rule--blue { top: 364px; }
  .rule--bottom.rule--blue { top: 486px; }
  .rule--bottom.rule--white { top: 495px; }
  .rule--bottom.rule--red { top: 504px; }

  .greeting { position: absolute; left: 0; right: 0; top: 384px; text-align: center; font-weight: 400;
              font-family: "Lobster", cursive; font-size: 80px; line-height: 1; white-space: nowrap; }
  .greeting__happy { color: var(--patriot-red); }
  .greeting__fourth { color: var(--star-white); }
  .greeting__july { color: var(--patriot-blue); }

  .back-message-panel { position: absolute; left: 0; top: 0; width: 390px; height: 548px;
    background:
      radial-gradient(ellipse 150px 120px at 60px 100px, rgba(110,20,30,0.6), transparent 70%),
      radial-gradient(ellipse 220px 140px at 300px 40px, rgba(70,25,110,0.65), transparent 75%),
      radial-gradient(ellipse 200px 120px at 150px 450px, rgba(70,40,30,0.45), transparent 75%),
      var(--card-dark); }
  .message-box { position: absolute; left: 22px; top: 156px; width: 346px; height: 256px; background: rgba(0,0,0,0.35); }
  .thanks { position: absolute; left: 0; width: 390px; top: 184px; text-align: center; font-weight: 400;
            font-family: "Lobster", cursive; font-size: 72px; line-height: 1; color: var(--patriot-red); }
  .thanks-sub { position: absolute; left: 0; width: 390px; top: 260px; text-align: center;
                font-size: 23px; color: var(--text-white); }
  .wishes { position: absolute; left: 0; width: 390px; top: 300px; text-align: center;
            font-size: 23px; line-height: 34px; color: var(--text-white); }

  .divider-blue { position: absolute; left: 393px; top: 0; width: 8px; height: 548px; background: var(--patriot-blue); }
  .divider-red { position: absolute; left: 405px; top: 61px; width: 13px; height: 418px; background: var(--patriot-red); }
  .address-side { position: absolute; left: 401px; top: 0; right: 0; bottom: 0;
    background: radial-gradient(ellipse 120px 160px at 20px 60px, rgba(200,180,240,0.35), transparent 70%),
                linear-gradient(180deg, #ffffff 55%, #f1f1f4 100%); }
  .stamp-box { position: absolute; left: 641px; top: 28px; width: 88px; height: 99px; background: var(--stamp-grey); }
  .address-line { position: absolute; left: 449px; width: 289px; height: 2px; background: var(--line-grey); }
  .address-line--1 { top: 241px; }
  .address-line--2 { top: 307px; }
  .address-line--3 { top: 379px; }
</style>
</head>
<body>
<svg width="0" height="0" style="position:absolute">
  <defs>
    <symbol id="star" viewBox="0 0 20 20">
      <polygon points="10,1 12.4,7.3 19,7.5 13.8,11.6 15.6,18 10,14.3 4.4,18 6.2,11.6 1,7.5 7.6,7.3" fill="#ffffff"/>
    </symbol>
  </defs>
</svg>

<section class="postcard postcard--front">
  <div class="front-artwork" role="img" aria-label="Dark patriotic backdrop with a bald eagle, waving American flags and fireworks"></div>

  <div class="firm-name firm-name--front"><span class="firm-name__dot"></span><span>Brightwater Counsel</span></div>

  <div class="star-row star-row--top" aria-hidden="true">
    <svg><use href="#star"/></svg><svg><use href="#star"/></svg><svg><use href="#star"/></svg>
    <svg><use href="#star"/></svg><svg><use href="#star"/></svg><svg><use href="#star"/></svg>
    <svg><use href="#star"/></svg><svg><use href="#star"/></svg><svg><use href="#star"/></svg>
  </div>
  <div class="rule rule--top rule--red"></div>
  <div class="rule rule--top rule--white"></div>
  <div class="rule rule--top rule--blue"></div>

  <h1 class="greeting">
    <span class="greeting__happy">Happy</span>
    <span class="greeting__fourth">4th of</span>
    <span class="greeting__july">July</span>
  </h1>

  <div class="rule rule--bottom rule--blue"></div>
  <div class="rule rule--bottom rule--white"></div>
  <div class="rule rule--bottom rule--red"></div>
  <div class="star-row star-row--bottom" aria-hidden="true">
    <svg><use href="#star"/></svg><svg><use href="#star"/></svg><svg><use href="#star"/></svg>
    <svg><use href="#star"/></svg><svg><use href="#star"/></svg><svg><use href="#star"/></svg>
    <svg><use href="#star"/></svg><svg><use href="#star"/></svg><svg><use href="#star"/></svg>
  </div>
</section>

<section class="postcard postcard--back">
  <div class="back-message-panel" role="img" aria-label="Dim backdrop of fireworks, a flag and an eagle in deep red and purple tones"></div>
  <div class="message-box"></div>
  <h2 class="thanks">Thank You</h2>
  <p class="thanks-sub">For Being A Valued Client!</p>
  <p class="wishes">Stay Safe And Enjoy Your<br>Independence Day<br>Celebrations!</p>

  <div class="address-side"></div>
  <div class="divider-blue"></div>
  <div class="divider-red"></div>
  <div class="firm-name firm-name--back"><span class="firm-name__dot"></span><span>Brightwater Counsel</span></div>
  <div class="stamp-box"></div>
  <div class="address-line address-line--1"></div>
  <div class="address-line address-line--2"></div>
  <div class="address-line address-line--3"></div>
</section>
</body>
</html>
```